Create Lanternfield HR Business Cards.

Create Business Cards for Lanternfield HR. 2 sided and Would like the back to have the logo.

Info for Business Card:
Address: 4827 Millbrook Ave Suite 230 Cleveland, Ohio 44987
Office Number: 216-555-0143
Mobile: 216-555-0192

Website: www.lanternfieldhr.example

Target Market(s)

Small to medium size businesses

Industry/Entity Type

Human Resources

Contact Information for Business Card

Company logo and information

Font styles to use
Serif
Sans Serif

Requirements
Must have
• Info for Business Card: Address: 4827 Millbrook Ave Suite 230 Cleveland, Ohio 44987 Office Number: 216-555-0143 Mobile: 216-555-0192 Website: www.lanternfieldhr.example

```html
<!DOCTYPE html>
<html lang="en">
<head>
<meta charset="utf-8">
<title>Lanternfield HR Business Cards</title>
<link href="https://fonts.googleapis.com/css2?family=Arimo:wght@400;700&display=swap" rel="stylesheet">
<style>
  :root {
    --navy: #241c66;
    --navy-deep: #1d1757;
    --navy-soft: #3a3290;
    --orange: #f07f12;
    --white: #ffffff;
    --backdrop: #e6e6e6;
  }
  * { box-sizing: border-box; margin: 0; padding: 0; }
  html, body { width: 1200px; height: 801px; overflow: hidden; }
  body {
    background: var(--backdrop);
    font-family: "Arimo", Arial, sans-serif;
    display: flex;
    align-items: center;
    justify-content: center;
    gap: 40px;
  }
  .card {
    position: relative;
    width: 520px;
    height: 297px;
    background: var(--navy);
    border-bottom: 4px solid var(--orange);
    color: var(--white);
    overflow: hidden;
  }
  .brand-name {
    font-weight: 700;
    color: var(--white);
    white-space: nowrap;
    text-align: center;
  }
  /* Front */
  .card-front .brand-name {
    position: absolute;
    top: 62px; left: 0; right: 0;
    font-size: 30px;
  }
  .identity {
    position: absolute;
    top: 150px; right: 268px;
    text-align: right;
  }
  .identity-name {
    color: var(--orange);
    font-weight: 700;
    font-size: 20px;
    letter-spacing: 0.5px;
    text-transform: uppercase;
  }
  .identity-role { font-size: 14px; margin-top: 2px; }
  .divider {
    position: absolute;
    left: 262px; top: 142px;
    width: 1px; height: 72px;
    background: rgba(255,255,255,0.6);
  }
  .contacts {
    position: absolute;
    left: 276px; top: 144px;
    list-style: none;
    font-size: 13px;
    line-height: 22px;
  }
  .contacts li { display: flex; align-items: center; gap: 8px; }
  .contacts svg { width: 12px; height: 12px; flex: none; }
  .address {
    position: absolute;
    bottom: 34px; left: 0; right: 0;
    text-align: center;
    font-size: 14px;
  }
  /* Back */
  .back-pattern {
    position: absolute; inset: 0;
    background: radial-gradient(circle at 70% 60%, var(--navy-soft) 0%, var(--navy) 55%, var(--navy-deep) 100%);
  }
  .card-back .brand-name {
    position: absolute;
    top: 50%; left: 50%;
    transform: translate(-50%, -50%);
    font-size: 22px;
  }
</style>
</head>
<body>
  <section class="card card-front" aria-label="Business card front">
    <p class="brand-name">Lanternfield HR</p>
    <div class="identity">
      <p class="identity-name">Daniel Mercer</p>
      <p class="identity-role">Manager</p>
    </div>
    <div class="divider"></div>
    <ul class="contacts">
      <li>
        <svg viewBox="0 0 12 12" aria-hidden="true"><path d="M2.5 1l2 2.2-1 1.2a7 7 0 003.1 3.1l1.2-1L10 8.5 8.8 10.8C5 10.5 1.5 7 1.2 3.2z" fill="#f07f12"/></svg>
        216-555-0143
      </li>
      <li>
        <svg viewBox="0 0 12 12" aria-hidden="true"><rect x="3" y="0.8" width="6" height="10.4" rx="1.2" fill="none" stroke="#f07f12" stroke-width="1.3"/><circle cx="6" cy="9.3" r="0.7" fill="#f07f12"/></svg>
        216-555-0192
      </li>
      <li>
        <svg viewBox="0 0 12 12" aria-hidden="true"><g fill="none" stroke="#f07f12" stroke-width="1.1"><circle cx="6" cy="6" r="5"/><ellipse cx="6" cy="6" rx="2.2" ry="5"/><path d="M1 6h10M2 3.3h8M2 8.7h8"/></g></svg>
        www.lanternfieldhr.example
      </li>
    </ul>
    <p class="address">4827 Millbrook Ave, Suite 230, Cleveland, Ohio 44987</p>
  </section>

  <section class="card card-back" aria-label="Business card back">
    <div class="back-pattern" role="img" aria-label="Embossed repeating brand pattern in deep violet tones"></div>
    <p class="brand-name">Lanternfield HR</p>
  </section>
</body>
</html>
```